Pharma Business needs a new careers template

We need a new job posting template to use for all of our open positions. We are in the pharma production business and want to elevate our job postings. The design should incorporate our company colours (namely blue and white).<br/><br/>The completed work should look professional, innovative and slightly quirky.<br/><br/>Feel free to familiarise yourself with some of our current designs on our website (www.morvita.com).<br/><br/>We have a few ideas of how we want the template to look like:<br/><br/>- We would like the design to incorporate various boxes that show different information like "Role Profile", "Benefits" etc.<br/><br/>- We would like to show some of our achievements in a special type of ellipses that remind of tablets or capsules. See a close example of another job posting incorporating similar design (but with circles instead of capsules/tablets) attached.<br/><br/>- We would like some of the main information like job location, contact phone etc to be shown after a corresponding icon. Example screenshot applied.<br/><br/>We have also attached an example job posting to give you an idea of what information our template should hold.

Industry/Entity Type

Pharmaceutical

Colors
33a6d7
ffffff
0393ce
3277b5

Requirements
Must have
• The file should be editable so we can freely fill it for each new position. We should also have it in PSD format.

```html
<!DOCTYPE html>
<html lang="en">
<head>
<meta charset="utf-8">
<title>Careers Flyer – Morvita Pharma</title>
<link href="https://fonts.googleapis.com/css2?family=Lato:wght@400;700;900&display=swap" rel="stylesheet">
<style>
:root{
  --navy:#2a44a0;
  --navy-deep:#22388a;
  --sky:#7cc4ee;
  --sky-soft:#a9d8f4;
  --sky-pale:#dff0fb;
  --ink:#2b4aa6;
  --black:#050505;
  --white:#ffffff;
  --stage:#e9ecf0;
}
*{margin:0;padding:0;box-sizing:border-box}
html,body{width:1200px;height:1200px;overflow:hidden;background:var(--stage);font-family:'Lato',sans-serif}
.flyer{position:absolute;left:190px;top:20px;width:859px;height:1216px;background:var(--white);transform:scale(.954);transform-origin:0 0;overflow:hidden;box-shadow:0 4px 18px rgba(0,0,0,.18)}
.abs{position:absolute}
.hiring{left:52px;top:16px;font-weight:900;font-size:26px;color:var(--navy);letter-spacing:-.3px}
.title-bar{left:0;top:52px;width:600px;height:48px;border-radius:0 24px 24px 0;background:linear-gradient(90deg,var(--navy) 0%,#3f6cc0 30%,#86cdf1 100%)}
.title-bar span{position:absolute;left:45px;top:2px;font-weight:900;font-size:40px;letter-spacing:8px;color:var(--white)}
.brand{left:690px;top:34px;width:150px;text-align:center;font-weight:900;font-size:26px;line-height:1.05;color:var(--navy)}
.brand-dot{display:block;width:14px;height:14px;border-radius:50%;background:var(--navy);margin:0 auto 6px}

.intro{left:20px;top:135px;width:440px;height:265px;background:var(--sky);border-radius:132px 0 0 132px;padding:32px 52px 0 40px;text-align:right;font-size:14.5px;line-height:18.2px;color:var(--navy-deep)}
.profile{left:420px;top:127px;width:420px;height:305px;background:var(--navy);border-radius:8px 152px 152px 0;color:var(--white);padding:20px 44px 0 16px}
.profile h2{font-weight:900;font-size:23px;margin-bottom:14px}
.profile p{font-size:14.5px;line-height:18.2px}
.profile svg{position:absolute;left:16px;top:240px}

.lower{left:0;top:458px;width:859px;height:758px;background:linear-gradient(180deg,var(--sky-pale) 0%,#cfe8f8 50%,var(--sky-soft) 100%)}
.pill{position:absolute;top:480px;height:630px;border-radius:148px;overflow:hidden}
.skills{left:25px;width:294px;background:linear-gradient(180deg,var(--sky) 0 182px,var(--navy) 182px)}
.skills .icon{position:absolute;left:115px;top:8px}
.skills h3{position:absolute;left:0;top:100px;width:294px;text-align:center;font-weight:900;font-size:22.5px;line-height:23px;color:var(--navy)}
.skills ul{position:absolute;left:40px;top:208px;width:232px;list-style:none;font-size:14.5px;line-height:18.2px;color:var(--white)}
.skills li{position:relative;padding-left:14px}
.skills li::before{content:"";position:absolute;left:0;top:7px;width:7px;height:7px;border-radius:50%;background:var(--sky)}

.benefits{left:330px;width:295px;background:linear-gradient(180deg,var(--black) 0 130px,var(--navy) 130px)}
.benefits .edge{position:absolute;right:6px;top:40px;width:30px;height:440px;border-radius:0 120px 60px 0;border-right:5px solid var(--sky)}
.benefits .icon{position:absolute;left:120px;top:38px}
.benefits h3{position:absolute;left:0;top:98px;width:295px;text-align:center;font-weight:900;font-size:21px;color:var(--white)}
.benefits .underline{position:absolute;left:98px;top:127px;width:98px;height:6px;border-radius:3px;background:var(--sky)}
.perks{position:absolute;left:36px;top:146px;width:222px;text-align:center;font-size:14px;line-height:17px;color:var(--white)}
.perk{margin-bottom:9px}
.perk i{display:block;width:28px;height:28px;margin:0 auto 3px;border-radius:50%;background:var(--white);position:relative}
.perk i b{position:absolute;inset:0;display:flex;align-items:center;justify-content:center;font-style:normal;font-weight:900;font-size:16px;color:var(--navy)}

.challenge-mark{left:720px;top:481px;width:44px;height:44px;border-radius:50%;background:var(--navy)}
.challenge-head{left:640px;top:528px;width:202px;text-align:center;font-weight:900;font-size:22px;line-height:23px;color:#2b5cb4}
.challenge-q{left:640px;top:596px;width:202px;text-align:center;font-weight:900;font-size:42px;color:#2b5cb4}
.challenge{left:642px;top:652px;width:196px;height:456px;border:4px solid var(--navy);border-radius:98px;background:var(--white);padding:38px 10px 0;text-align:center;font-size:14.5px;line-height:18.2px;color:var(--ink)}
.challenge .bar{display:block;width:58px;height:6px;border-radius:3px;background:var(--sky);margin:4px auto 0}

.footer{left:0;top:1145px;width:859px;height:71px;background:var(--navy)}
.site{left:50px;top:1122px;width:475px;height:40px;border-radius:20px;background:var(--white);display:flex;align-items:center;justify-content:center;gap:10px;font-weight:900;font-size:23px;color:var(--navy)}
.contact{display:flex;align-items:center;gap:8px;font-size:17px;color:var(--white)}
.phone{left:55px;top:1180px}
.mail{left:348px;top:1180px}
.address{left:620px;top:1162px;align-items:flex-start;line-height:21px}
</style>
</head>
<body>
<div class="flyer">
  <div class="abs hiring">WE ARE HIRING!</div>
  <div class="abs title-bar"><span>JOB TITLE</span></div>
  <div class="abs brand"><span class="brand-dot"></span>Morvita<br>Pharma</div>

  <div class="abs intro">Habitasse porta luctus porta. Aptent augue. Justo aliquet urna justo. Inceptos ligula elit aenean maecenas montes ullamcorper commodo volutpat Massa aliquam velit interdum viverra congue malesuada lacus lobortis egestas malesuada blandit nec facilisis. Fermentum tempor arcu litora fringilla, quis aenean sagittis feugiat a pretium hendrerit sociosqu mattis, maecenas.Turpis lorem. Aliquet nibh sociis mus facilisi interdum aliquet aenean sem vulputate natoque. Malesuada rutrum sociosqu sociosqu litora nunc ornare feugiat volutpat feugiat natoque dictumst scelerisque sociis ornare Eget inceptos quam interdum.</div>

  <div class="abs profile">
    <h2>ROLE PROFILE</h2>
    <p>Velit Commodo, ultrices proin tellus montes magnis mi porttitor metus sociis condimentum dis platea. Ad consectetuer laoreet euismod ad donec tellus elit ad metus lectus. Sit pretium quis imperdiet velit turpis diam urna torquent ante phasellus nascetur per euismod ultrices consectetuer a. Sollicitudin lobortis scelerisque vel senectus id, pharetra iaculis non sem id nam odio fames facilisi quam integer condimentum rutrum pulvinar inceptos. Montes id nonummy platea,mattis proin cum.</p>
    <svg width="345" height="50" viewBox="0 0 345 50"><path d="M0 40 L0 48 C150 48 280 40 340 6 C270 34 150 38 0 40Z" fill="#fff"/></svg>
  </div>

  <div class="abs lower"></div>

  <section class="pill skills">
    <svg class="icon" width="64" height="92" viewBox="0 0 64 92">
      <polygon points="32,2 37,14 50,15 40,23 43,36 32,29 21,36 24,23 14,15 27,14" fill="none" stroke="#2a44a0" stroke-width="4"/>
      <circle cx="32" cy="55" r="8" fill="none" stroke="#2a44a0" stroke-width="4"/>
      <path d="M6 50 C10 72 22 86 32 86 C42 86 54 72 58 50" fill="none" stroke="#2a44a0" stroke-width="5" stroke-linecap="round"/>
    </svg>
    <h3>TO BE SUCCESSFUL<br>IN THIS ROLE<br>YOU SHOULD HAVE:</h3>
    <ul>
      <li>Cubilia. Porta. Morbi aliquet aptent Aenean nostra purus.</li>
      <li>Rhoncus vitae mus fermentum placerat placerat libero.</li>
      <li>Interdum, dapibus aliquet dignissim hac fusce non. Consectetuer.</li>
      <li>Quam hac, ornare hendrerit ultricies.</li>
      <li>Netus parturient elementum, nisi purus dui.</li>
      <li>Justo sodales, suspendisse fermentum, quisque fermentum quisque pulvinar.</li>
      <li>Convallis lectus feugiat suspendisse ullamcorper nonummy duis pretium.</li>
      <li>Eget pretium per tempor natoque. Quisque.</li>
    </ul>
  </section>

  <section class="pill benefits">
    <div class="edge"></div>
    <svg class="icon" width="56" height="52" viewBox="0 0 56 52">
      <rect x="3" y="12" width="38" height="38" fill="none" stroke="#4aa8e0" stroke-width="5"/>
      <path d="M10 28 L21 40 L52 4" fill="none" stroke="#4aa8e0" stroke-width="7"/>
    </svg>
    <h3>BENEFITS</h3>
    <div class="underline"></div>
    <div class="perks">
      <div class="perk"><i><b>•</b></i>Nonummy fermentum nec dictumst et.</div>
      <div class="perk"><i><b>!</b></i>Venenatis. Aenean ac. Commodo volutpat dolor libero mus.</div>
      <div class="perk"><i><b>★</b></i>Cras consequat, non tempor justo.</div>
      <div class="perk"><i><b>♥</b></i>Natoque potenti Hymenaeos ad tristique torquent ultrices. Nec donec. Eu.</div>
      <div class="perk"><i><b>✦</b></i>Ac consequat ridiculus convallis curae; porttitor.</div>
      <div class="perk"><i><b>$</b></i>Lobortis non hendrerit taciti sed. Cursus.</div>
    </div>
  </section>

  <div class="abs challenge-mark"></div>
  <div class="abs challenge-head">CHALLENGED<br>BY THIS CAREER<br>OPPORTUNITY</div>
  <div class="abs challenge-q">?</div>
  <div class="abs challenge">Curae; eros cubilia suspendisse netus turpis laoreet nonummy vivamus scelerisque rutrum. Risus porttitor semper erat lorem ante orci cum natoque mauris lobortis. Velit semper aliquet. Metus proin ullamcorper augue urna. Eros taciti maecenas est, aliquam parturient etiam gravida nullam molestie. Sem imperdiet. Porta praesent sit. Vitae pede luctus et potenti ac augue primis cum vel. Blandit scelerisque tincidunt tincidunt luctus pretium eleifend.<span class="bar"></span></div>

  <div class="abs footer"></div>
  <div class="abs site">
    <svg width="24" height="24" viewBox="0 0 24 24" fill="none" stroke="#2a44a0" stroke-width="2"><circle cx="12" cy="12" r="10"/><ellipse cx="12" cy="12" rx="4.5" ry="10"/><path d="M2 12h20M4 7h16M4 17h16"/></svg>
    www.morvitapharma.bg
  </div>
  <div class="abs contact phone">
    <svg width="20" height="20" viewBox="0 0 24 24"><path d="M5 3l4 0 2 5-2.5 1.5a12 12 0 0 0 6 6L16 13l5 2v4c0 1-1 2-2 2C10 21 3 14 3 5c0-1 1-2 2-2z" fill="none" stroke="#fff" stroke-width="2"/></svg>
    +359 2 555 01 230/1/2
  </div>
  <div class="abs contact mail">
    <svg width="24" height="18" viewBox="0 0 24 18" fill="none" stroke="#fff" stroke-width="2"><rect x="1" y="1" width="22" height="16"/><path d="M1 1l11 9 11-9"/></svg>
    office@morvita.com
  </div>
  <div class="abs contact address">
    <svg width="18" height="24" viewBox="0 0 18 24"><path d="M9 0C4 0 0 4 0 9c0 6 9 15 9 15s9-9 9-15c0-5-4-9-9-9z" fill="#fff"/><circle cx="9" cy="9" r="3.5" fill="#2a44a0"/></svg>
    <span>48 Lipa Str.<br>1320 Bankya, Bulgaria</span>
  </div>
</div>
</body>
</html>
```